skyROAMER Helicopter Tour WordPress Website Design

SkyROAMER (skyroamer-example.com) is a premium helicopter tour company offering scenic flights in two Florida cities: Tampa and Sarasota. We are seeking a full Wordpress website redesign that is modern, upbeat, inviting, and highly conversion‑focused. The new site should feel energetic and trustworthy, reflect the excitement of helicopter sightseeing, and maintain our recognizable SkyROAMER color palette—while updating the overall look to feel fresh, clean, and current.
The website must be SEO‑friendly, mobile‑optimized, and easy to navigate. It should highlight our 5‑star customer reviews, showcase our tours clearly, and integrate seamlessly with TripLantern for instant online booking. The design should support a premium aviation experience while remaining friendly and accessible to tourists, families, couples, and adventure seekers.

These elements are essential and must be included in the design:

Brand & UX:
- Modern, upbeat, inviting design
- SEO‑friendly structure and layout
- Easy navigation and clear user flow
- Light grey “SR” background logo watermark (as used on current site)
- Clean, aviation‑inspired typography and layout

Conversion Features:
- Instant booking above the fold (TripLantern integration)
- Live Pindle Ratings carousel
- Tour comparison table (duration, route, price, etc.)
- FAQ expandable section
- Gift Cards page (highlighted as a major offering)
- What to Expect timeline (Arrive → Check‑In → Safety Briefing → Flight → Photos)
- Weather transparency widget (clear messaging about weather‑dependent flights

Content Structure:
- Separate pages for Tampa, Sarasota, and Gender Reveal Flights
- Pilot/Team profiles with short bios
- Highlighted features:
- Doors‑Off option
- Sunset flights
- Romantic packages
- Champagne add‑ons

Colors:
Use the existing SkyROAMER palette as the foundation, but modernize it.
- Background: Clean with the light grey “SR” watermark integrated tastefully.
The overall color direction should feel bright, premium, energetic, and trustworthy

Target Market(s)

Tourists visiting Tampa or Sarasota, Families looking for memorable activities, Couples seeking romantic experiences (sunset flights, proposals, anniversaries), Adventure seekers and content creators, Locals celebrating birthdays, holidays, or special occasions, Gender reveal clients looking for a unique aerial reveal experience

Industry/Entity Type

Travel & Tourism / Aviation / Helicopter Tours / Experience‑based Activities

Requirements
Must have
• These elements are essential and must be included in the design: Brand & UX - Modern, upbeat, inviting design / SEO‑friendly structure and layout / Easy navigation and clear user flow / Light grey “SR” background logo watermark (as used on current site) / Clean, aviation‑inspired typography and layout
Nice to have
• Interactive route map showing flight paths / Subtle motion or parallax effects in hero sections / Animated icons or micro‑interactions / Social media integration (Photavia grid, ClipNest clips) / Sticky mobile booking bar / Video header or short aerial footage loop / Subtle aviation‑themed graphic elements (rotor blur, sky gradients, etc.
Should not have
• No dark, heavy, or overly moody themes / No outdated fonts or overly playful typography / No cluttered layouts or excessive text blocks / No stocky, generic tourism imagery / No slow‑loading animations or heavy effects that hurt SEO

```html
<!DOCTYPE html>
<html lang="en">
<head>
<meta charset="UTF-8">
<title>What to Expect – Helicopter Tours</title>
<link href="https://fonts.googleapis.com/css2?family=Poppins:wght@600;700&family=Roboto:wght@400;500&display=swap" rel="stylesheet">
<style>
:root{
  --blue:#0a7cff;
  --teal:#17a2b8;
  --green:#28a745;
  --yellow:#ffc107;
  --pink:#e83e8c;
  --ink:#2b2f33;
  --muted:#6c757d;
  --card:#ffffff;
}
*{margin:0;padding:0;box-sizing:border-box}
html,body{width:927px;height:1200px;overflow:hidden;background:#fff}
body{position:relative;font-family:'Roboto',sans-serif;color:var(--ink);
  background:
    radial-gradient(circle at 780px 380px, rgba(214,232,253,.22), transparent 150px),
    radial-gradient(circle at 130px 1130px, rgba(214,232,253,.35), transparent 150px),
    #fff;}
.feature-band{position:absolute;left:7px;top:0;width:913px;height:185px;background:linear-gradient(180deg,#d9e9fd,#d0e4fc)}
.feature-card{position:absolute;left:50px;top:22px;width:813px;height:109px;background:var(--card);border-radius:12px;box-shadow:0 6px 16px rgba(40,80,140,.08);display:flex}
.feature{flex:1;text-align:center;padding-top:20px}
.feature svg{width:26px;height:26px;display:block;margin:0 auto}
.feature-title{font-size:11px;font-weight:500;margin-top:10px;color:#23272b}
.feature-text{font-size:9.5px;color:var(--muted);margin-top:7px}
.expect-head{position:absolute;left:0;top:230px;width:927px;text-align:center}
.expect-head h2{font-family:'Poppins',sans-serif;font-weight:700;font-size:32px;line-height:44px;color:#24282c}
.expect-head p{font-size:13.4px;line-height:19px;color:var(--muted);margin-top:8px}
.timeline-line{position:absolute;left:463px;top:362px;width:2px;height:716px;background:linear-gradient(180deg,var(--blue),var(--teal))}
.step{position:absolute;width:364px;height:117px;background:var(--card);border-radius:10px;box-shadow:0 5px 14px rgba(0,0,0,.07);padding:16px}
.step.left{left:57px;text-align:right}
.step.right{left:506px;text-align:left}
.step-head{display:flex;align-items:center;gap:12px;height:42px}
.step.left .step-head{flex-direction:row-reverse}
.step-num{width:42px;height:42px;border-radius:50%;color:#fff;font-family:'Poppins',sans-serif;font-weight:600;font-size:14.5px;display:flex;align-items:center;justify-content:center;flex-shrink:0}
.step-title{font-family:'Poppins',sans-serif;font-weight:700;font-size:16px;color:var(--ink)}
.step-text{font-size:10.7px;line-height:16px;color:var(--muted);margin-top:14px}
.cta{position:absolute;left:353px;top:1121px;width:221px;height:40px;background:var(--blue);color:#fff;border-radius:4px;font-size:12px;font-weight:500;display:flex;align-items:center;justify-content:center;gap:8px;text-decoration:none;box-shadow:0 6px 14px rgba(10,124,255,.25)}
</style>
</head>
<body>
<section class="feature-band">
  <div class="feature-card">
    <div class="feature">
      <svg viewBox="0 0 26 26"><path d="M3 23V6l9-3v20z" fill="var(--blue)"/><path d="M14 5h6v16h3" stroke="var(--blue)" stroke-width="2.4" fill="none"/><circle cx="9" cy="13" r="1.2" fill="#fff"/></svg>
      <div class="feature-title">Doors-Off Option</div>
      <div class="feature-text">Unobstructed aerial photography</div>
    </div>
    <div class="feature">
      <svg viewBox="0 0 26 26"><g fill="var(--yellow)"><polygon points="13,1 15,6 11,6"/><polygon points="13,25 15,20 11,20"/><polygon points="1,13 6,11 6,15"/><polygon points="25,13 20,11 20,15"/><polygon points="4.5,4.5 9,7 7,9"/><polygon points="21.5,21.5 17,19 19,17"/><polygon points="21.5,4.5 19,9 17,7"/><polygon points="4.5,21.5 7,17 9,19"/></g><circle cx="13" cy="13" r="6" fill="none" stroke="var(--yellow)" stroke-width="2.5"/></svg>
      <div class="feature-title">Sunset Flights</div>
      <div class="feature-text">Golden hour magic</div>
    </div>
    <div class="feature">
      <svg viewBox="0 0 26 26"><path d="M13 23C5 17 1 13 1 8.5 1 5 3.8 2.5 7 2.5c2.6 0 4.6 1.6 6 3.6 1.4-2 3.4-3.6 6-3.6 3.2 0 6 2.5 6 6C25 13 21 17 13 23z" fill="var(--pink)"/></svg>
      <div class="feature-title">Romantic Packages</div>
      <div class="feature-text">Perfect for proposals</div>
    </div>
    <div class="feature">
      <svg viewBox="0 0 26 26"><g fill="var(--green)"><path d="M3 4l7 2-1 6a3 3 0 0 1-4-1z"/><path d="M23 4l-7 2 1 6a3 3 0 0 0 4-1z"/><rect x="5.6" y="12" width="1.8" height="9" transform="rotate(-12 6.5 16)"/><rect x="18.6" y="12" width="1.8" height="9" transform="rotate(12 19.5 16)"/><rect x="2" y="21" width="7" height="2" rx="1"/><rect x="17" y="21" width="7" height="2" rx="1"/></g><circle cx="13" cy="3" r="1.2" fill="var(--green)"/></svg>
      <div class="feature-title">Champagne Add-On</div>
      <div class="feature-text">Celebrate in style</div>
    </div>
  </div>
</section>

<header class="expect-head">
  <h2>What to Expect</h2>
  <p>Your journey from arrival to takeoff is designed for comfort, safety, and excitement.<br>Here's your step-by-step experience.</p>
</header>

<div class="timeline-line"></div>

<article class="step left" style="top:362px">
  <div class="step-head"><span class="step-num" style="background:var(--blue)">1</span><h3 class="step-title">Arrive &amp; Check-In</h3></div>
  <p class="step-text">Arrive 15 minutes before your scheduled flight. Our friendly team will greet you and handle check-in quickly and efficiently.</p>
</article>
<article class="step right" style="top:512px">
  <div class="step-head"><span class="step-num" style="background:var(--teal)">2</span><h3 class="step-title">Safety Briefing</h3></div>
  <p class="step-text">Your pilot will provide a comprehensive safety briefing and answer any questions you have about the flight and helicopter.</p>
</article>
<article class="step left" style="top:661px">
  <div class="step-head"><span class="step-num" style="background:var(--green)">3</span><h3 class="step-title">Board &amp; Buckle Up</h3></div>
  <p class="step-text">Board your helicopter and get comfortable. We'll ensure everyone is properly secured with headsets for clear communication.</p>
</article>
<article class="step right" style="top:811px">
  <div class="step-head"><span class="step-num" style="background:var(--yellow);color:var(--ink)">4</span><h3 class="step-title">Soar &amp; Explore</h3></div>
  <p class="step-text">Experience the thrill of liftoff! Your pilot will narrate the tour, pointing out landmarks and ensuring you capture perfect photos.</p>
</article>
<article class="step left" style="top:961px">
  <div class="step-head"><span class="step-num" style="background:var(--pink)">5</span><h3 class="step-title">Share Your Experience</h3></div>
  <p class="step-text">After landing, share your incredible photos and memories. Don't forget to leave us a review and tag us on social media!</p>
</article>

<a class="cta" href="#">Learn More About Your Flight
  <svg width="12" height="12" viewBox="0 0 12 12"><path d="M1 6h9M6.5 2.5 10 6l-3.5 3.5" stroke="#fff" stroke-width="1.8" fill="none" stroke-linecap="round" stroke-linejoin="round"/></svg>
</a>
</body>
</html>
```